Gardener needs an exciting new flyer design.

I'm a passionate gardener that requires a custom flyer design for a owner operator gardening business. Design will be for a DL flyer. I'm based on the Sunshine coast in Queensland Australia. My target audience is the residential market on the Sunshine coast. Business name is Tollmere Yards. My services are, lawn mowing, weeding, Eco Friendly fertilizing, green waste removal, Mulching, tree and shrub pruning, Full garden makeovers, hedging, pressure cleaning, privacy screening, Timber deck rejuvenation, Planting, Turf preparation and installation, and much more. Free no obligation quotes, reliable and friendly service, great rates. 12 years experience. Web www.tollmereyards.com.au - Phone 0418527036 - Email kip@tollmereyards.com.au I would like the design to portray a friendly and professional approach.

Target Market(s)

Residential

Industry/Entity Type

Gardener

Font styles to use
Serif

Colors
9ccb3b
abd037
3176b5

Requirements
Must have
• my services, my logo, my contact details,

```html
<!DOCTYPE html>
<html lang="en">
<head>
<meta charset="utf-8">
<title>Tollmere Yards – DL Flyer</title>
<link href="https://fonts.googleapis.com/css2?family=Almendra:wght@700&family=Cinzel:wght@400;600;700&display=swap" rel="stylesheet">
<style>
  :root {
    --lime: #a6cf3a;
    --lime-dark: #9ccb3b;
    --leaf: #3d8f2e;
    --sky: #4389c4;
    --sky-deep: #3176b5;
    --white: #ffffff;
    --ink: #161616;
  }
  * { margin: 0; padding: 0; box-sizing: border-box; }
  html, body { width: 1200px; height: 2545px; overflow: hidden; }
  body { background: var(--lime); font-family: "Cinzel", Georgia, serif; }

  .flyer { position: relative; width: 1200px; height: 2545px; overflow: hidden; }

  .header {
    position: absolute; left: 0; top: 0; width: 1200px; height: 914px;
    background: var(--lime);
  }
  .brand-mark {
    position: absolute; left: 470px; top: 150px; width: 260px; height: 260px;
    border-radius: 50%; background: var(--leaf);
  }
  .brand-name {
    position: absolute; left: 0; top: 535px; width: 1200px; text-align: center;
    font-family: "Almendra", Georgia, serif; font-weight: 700;
    font-size: 104px; line-height: 1; color: var(--leaf);
  }
  .phone-pill {
    position: absolute; left: 180px; top: 712px; width: 841px; height: 118px;
    border-radius: 52px; background: var(--sky);
    box-shadow: 0 6px 8px rgba(0,0,0,0.35);
    display: flex; align-items: center; justify-content: center;
    color: var(--white); font-weight: 700; font-size: 70px; letter-spacing: 2px;
    text-shadow: 0 3px 4px rgba(0,0,0,0.3);
  }

  .services {
    position: absolute; left: 0; top: 914px; width: 1200px; height: 1392px;
    background: var(--sky);
  }
  .services-tab {
    position: absolute; left: 405px; top: 884px; width: 390px; height: 58px;
    border-radius: 0 0 30px 30px; background: var(--lime);
    display: flex; align-items: center; justify-content: center;
    color: var(--sky-deep); font-weight: 600; font-size: 38px; letter-spacing: 1px;
  }
  .service-list {
    position: absolute; left: 0; top: 1010px; width: 1200px; list-style: none;
  }
  .service-list li {
    height: 97.5px; display: flex; align-items: center; justify-content: center;
    color: var(--white); font-size: 46px; letter-spacing: 1.5px;
    text-shadow: 0 3px 4px rgba(0,0,0,0.35);
  }
  .service-list li::before,
  .service-list li::after {
    content: ""; width: 0; height: 0; margin: 0 34px;
    border-top: 6px solid transparent; border-bottom: 6px solid transparent;
    border-left: 8px solid var(--white);
  }

  .contact {
    position: absolute; left: 0; top: 2306px; width: 1200px; height: 239px;
    background: var(--lime);
    display: flex; flex-direction: column; align-items: center; justify-content: center;
    gap: 4px; color: var(--ink); font-weight: 600; font-size: 43px; letter-spacing: 1.5px;
  }
</style>
</head>
<body>
  <main class="flyer">
    <header class="header">
      <div class="brand-mark"></div>
      <h1 class="brand-name">Tollmere Yards</h1>
      <div class="phone-pill">PHONE: 0418527036</div>
    </header>

    <section class="services">
    </section>
    <div class="services-tab">OUR SERVICES:</div>
    <ul class="service-list">
      <li>LAWN MOWING</li>
      <li>WEEDING</li>
      <li>ECO FRIENDLY FERTILIZING</li>
      <li>GREEN WASTE REMOVAL</li>
      <li>MULCHING</li>
      <li>TREE AND SHRUB PRUNING</li>
      <li>FULL GARDEN MAKEOVERS</li>
      <li>HEDGING</li>
      <li>PRESSURE CLEANING</li>
      <li>PRIVACY SCREENING</li>
      <li>TIMBER DECK REJUVENATION</li>
      <li>PLANTING</li>
      <li>TURF PREPARATION AND INSTALLATION</li>
    </ul>

    <footer class="contact">
      <p class="contact-email">EMAIL: KIP@TOLLMEREYARDS.COM.AU</p>
      <p class="contact-web">WEB: WWW.TOLLMEREYARDS.COM.AU</p>
    </footer>
  </main>
</body>
</html>
```